Lotvantage.com Webpage Design

Design Brief for lotvantage.com (Copy of Brief also in attached Word file)

Name of Website- lotvantage.com (existing logo and look & feel of website to be changed)

Logo - Finalised. The logo files are attached with the brief as “logo.jpeg”. The “Blue- Grey” version of the logo is for use on lighter backgrounds and the “Orange-White” version of the logo is for use on darker backgrounds. (A full Black version of the logo is also attached). Both versions may be used in different parts of the website. All attached files are in .png format.
Status - The website in functional and is undergoing user trials. However, we want to improve the look & feel of the website so at it seems
a. cotemporary,
b. Easy to Navigate
c. professional and
d. Vibrant.

Please visit ‘lotvantage.com’ to check out the website and its functionalities – please use it only as a reference for the features & functions to be provided, however the designer should use a ‘Free Hand’ in designing the composition of various parts of the webpage without getting too influenced by the existing design

Objective of the Website ‘lotvantage.com –
a. It is a portal focussed on listing of ‘Retail’ specific real-estate properties by developers, owners and realty brokers. The properties shall listed under the following four categories-
i. Retail Malls
ii. Shopping Complexes
iii. High-street shops
iv. Retail Warehouses
*refer lotvantage.com for better clarity

b. The abovementioned properties shall be listed either for ‘Sale’ or ‘rent\lease’ or both

c. Users shall visit the site in case they wish to acquire a retail \ shop space either on ‘sale’ or ‘rent’. These Users would be able to specify the ‘Search Criteria’ through the tool-bars provided on the website – the ‘Search Criteria’ shall comprise of ‘Type of space category’, ‘City’, ‘Locality’, transaction type ie ‘Rent \ Sale’ and ‘Area Range’

d. The main revenue model for the website shall be listing fee ( or advertising charges ) payable by those listing their properties on the website.

Three Main Pages of Website (lotvantage.com) that need to be designed -
a. Main Home Page (visit the web link - http://lotvantage.com/ ) - The main home page has the “Search Toolbar” for specifying of Search Criteria by the User. It shall also have the following features & functions-
i. Main Advertising Banner
ii. Featured Projects
iii. New Launches
iv. Toolbar with buttons – ‘Advertise with Us’, ‘Listings Alert’, ‘Lot Mavens’, ‘Advertiser Login’

b. Property Listings Page (visit the web link - http://lotvantage.com/gurgaon-in-india ) - The List of property options that match the Criteria specified by the ‘User’ get displayed on this page.

c. Property Detail Page - When the ‘User’ clicks on the “More….” Button on the ‘Property Listings Page’ (given in point b. above) the web page with the details of the property opens. (For Example – visit the web link - http://lotvantage.com/brevo-Shopping-Complex-brevo-quadrel-gurgaon-636 )

Note:- Please refer to attached ‘Shopping’ related images the designer may use them on the website to provide a look & feel of retail if required – either separately or rotate in a single window

Target Market(s)

Retailers & Investors looking for retail space, Real Estate Brokers, Developers

Industry/Entity Type

Advertising

Number of Pages Required

3 page

Requirements
Must have
• Refer to existing site lotvantage.com -- all the existing functionalities are a must have.
Nice to have
• The Designer may use the retail related images on the website if required for making it more vibrant. Refer attached images Shopping(1-6).jpg

```html
<!DOCTYPE html>
<html lang="en">
<head>
<meta charset="utf-8">
<title>Lotvantage.com – Retail Space Portal</title>
<link href="https://fonts.googleapis.com/css2?family=Arimo:wght@400;700&family=Open+Sans:wght@400;600;700&display=swap" rel="stylesheet">
<style>
:root{
  --orange:#f0962b;
  --orange-dark:#e0841a;
  --dark:#1e1e1e;
  --dark-2:#161616;
  --page:#efefef;
  --panel:#ffffff;
  --panel-grey:#f4f4f4;
  --text:#222222;
  --muted:#8a8a8a;
  --line:#d9d9d9;
}
*{box-sizing:border-box;margin:0;padding:0}
html,body{width:1200px;height:2542px;overflow:hidden}
body{background:var(--page);font-family:"Arimo",Arial,sans-serif;color:var(--text);position:relative}

/* header */
.site-header{position:absolute;left:0;top:0;width:1200px;height:124px;background:var(--dark);border-top:3px solid var(--orange)}
.city-links{position:absolute;right:32px;top:14px;display:flex;gap:19px;font-size:10px;color:#6d6d6d}
.brand{position:absolute;left:102px;top:50px;display:flex;align-items:center;gap:10px}
.brand-dot{width:30px;height:30px;border-radius:50%;background:var(--orange)}
.brand-name{font-size:30px;font-weight:700;color:#ffffff;letter-spacing:-0.5px;line-height:1}
.brand-tag{position:absolute;left:142px;top:88px;font-size:7px;font-weight:700;color:var(--orange);letter-spacing:0.6px}
.main-nav{position:absolute;right:88px;top:66px;display:flex;align-items:center;gap:36px;font-size:13px;color:#ffffff}
.main-nav .active{color:var(--orange)}
.login-btn{background:var(--orange);color:#fff;padding:7px 12px;border-radius:2px;font-size:12px}

/* hero */
.hero{position:absolute;left:0;top:124px;width:1200px;height:569px;
  background:linear-gradient(120deg,#6d6454 0%,#a89a82 35%,#d9c7a8 55%,#b58a5e 75%,#5e4a36 100%)}
.hero-caption{position:absolute;left:98px;top:213px;width:446px;height:130px;background:rgba(255,255,255,0.82);padding:20px 36px}
.hero-caption h1{font-size:25px;font-weight:700;color:#111;line-height:30px}
.hero-caption h1 span{color:var(--orange)}
.hero-caption p{font-size:11.5px;line-height:19px;color:#333;margin-top:8px;white-space:nowrap}
.read-more{position:absolute;left:98px;top:351px;width:73px;height:28px;background:var(--orange);color:#fff;font-size:10px;display:flex;align-items:center;justify-content:center}
.hero-arrow{position:absolute;top:261px;width:46px;height:46px;border:2px solid #fff;border-radius:50%;background:rgba(0,0,0,0.15)}
.search-tab{position:absolute;left:98px;top:527px;width:229px;height:42px;background:var(--dark);color:#fff;font-size:16px;font-weight:700;display:flex;align-items:center;gap:20px;padding-left:16px}

/* content column */
.content{position:absolute;left:98px;top:693px;width:1004px;height:1558px;background:var(--panel)}
.search-panel{position:absolute;left:0;top:0;width:1004px;height:190px;border-bottom:1px solid var(--line)}
.field{position:absolute;font-size:11px;color:#333}
.field label{display:block;margin-bottom:10px}
.select{width:222px;height:28px;border:1px solid #cfcfcf;font-size:10px;color:#555;padding:7px 18px;position:relative;background:#fff}
.select::after{content:"";position:absolute;right:0;top:0;width:22px;height:26px;border-left:1px solid #ddd;background:#f3f3f3}
.input{width:222px;height:29px;border:1px solid #cfcfcf;font-size:10px;color:#555;padding:8px 16px}
.search-btn{position:absolute;left:268px;top:129px;width:80px;height:29px;background:var(--orange);color:#fff;font-size:11px;display:flex;align-items:center;justify-content:center}
.format-note{position:absolute;left:377px;top:138px;font-size:9px;color:#444}
.format-note a{color:var(--orange);text-decoration:underline}

.about{position:absolute;left:0;top:190px;width:1004px;height:300px;background:var(--panel-grey)}
.section-title{position:absolute;left:0;width:1004px;text-align:center;font-size:21px;font-weight:700;color:#111;text-transform:uppercase}
.section-title span{color:var(--orange)}
.section-title::after{content:"";display:block;width:40px;height:1px;background:#999;margin:6px auto 0}
.about-text{position:absolute;left:40px;top:84px;width:924px;text-align:center;font-size:9.5px;line-height:19px;color:#777}
.category{position:absolute;top:150px;width:220px;text-align:center}
.category svg{display:block;margin:0 auto}
.category h3{font-size:15px;font-weight:700;color:#111;margin-top:12px}
.category p{font-size:10px;color:#888;margin-top:3px}

.card{position:absolute;width:218px;height:282px;border:1px solid #e2e2e2;background:#fff}
.card-photo{position:relative;height:132px}
.city-tag{position:absolute;left:0;bottom:0;background:rgba(20,20,20,0.85);color:#fff;font-size:12px;padding:4px 18px 4px 10px}
.card-body{padding:20px 18px}
.card-name{font-size:15px;font-weight:700;color:var(--orange)}
.card-line{font-size:12px;color:#666;line-height:21px}
.view-btn{display:inline-flex;align-items:center;justify-content:center;width:104px;height:29px;background:var(--orange);color:#fff;font-size:11px;font-weight:700;margin-top:7px}

.launch{position:absolute;top:1282px;width:209px}
.launch .card-photo{height:130px}
.launch-name{font-size:15px;font-weight:700;color:var(--orange);margin-top:12px;margin-left:3px}
.launch-sub{font-size:11px;color:#555;margin-left:3px}
.launch .view-btn{margin-top:8px;margin-left:3px}
.carousel-arrow{position:absolute;top:1333px;width:21px;height:28px;background:#d9d9d9}

/* footer */
.site-footer{position:absolute;left:0;top:2251px;width:1200px;height:241px;background:var(--dark);border-top:4px solid var(--orange);font-family:"Open Sans",Arial,sans-serif}
.foot-col{position:absolute;top:40px}
.foot-col h4{font-size:16px;font-weight:700;color:#fff;text-transform:uppercase;letter-spacing:0.3px}
.foot-col p,.foot-col li{font-size:11px;line-height:22px;color:#8c8c8c;list-style:none}
.social{display:flex;gap:10px;margin-top:18px}
.social span{width:27px;height:27px;border:1.5px solid #ddd;border-radius:50%}
.alert-form{display:flex;margin-top:14px}
.alert-form .email{width:170px;height:37px;border:1px solid #666;font-size:11px;color:#aaa;padding:10px}
.alert-form .signup{width:79px;height:37px;background:var(--orange);color:#fff;font-size:11px;font-weight:700;display:flex;align-items:center;justify-content:center}
.copyright{position:absolute;left:0;top:2492px;width:1200px;height:50px;background:var(--dark-2);color:#777;font-size:11px;text-align:center;line-height:50px;border-top:1px solid #2a2a2a;font-family:"Open Sans",Arial,sans-serif}
</style>
</head>
<body>

<header class="site-header">
  <nav class="city-links">
    <span>Bangalore</span><span>Chennai</span><span>Greater Noida</span><span>Gurgaon</span><span>Hyderabad</span><span>Jaipur</span><span>Kharar</span><span>Kolkata</span><span>Mumbai</span><span>Noida</span><span>Pune</span><span>Surat</span>
  </nav>
  <div class="brand"><span class="brand-dot"></span><span class="brand-name">lotvantage</span></div>
  <div class="brand-tag">INDIA'S LEADING PORTAL FOR RETAIL SPACE</div>
  <nav class="main-nav">
    <span class="active">Home</span><span>Advertise with Us</span><span>Listings Alert</span><span>Lot Mavens</span>
    <span class="login-btn">Advertiser Login ▾</span>
  </nav>
</header>

<section class="hero" role="img" aria-label="Banner photograph: a joyful shopper in an orange outfit holding colourful shopping bags inside a mall atrium">
  <div class="hero-caption">
    <h1>find <span>retail</span> space</h1>
    <p>Lorem ipsum dolor sit amet, consectetuer adipiscing elit. Aenean comm<br>ligula eget dolor. Aenean massa. Cum sociis natoque penatibus</p>
  </div>
  <div class="read-more">Read More</div>
  <div class="hero-arrow" style="left:26px">
    <svg width="42" height="42" viewBox="0 0 42 42"><path d="M24 14l-7 7 7 7" fill="none" stroke="#fff" stroke-width="2"/></svg>
  </div>
  <div class="hero-arrow" style="left:1125px">
    <svg width="42" height="42" viewBox="0 0 42 42"><path d="M18 14l7 7-7 7" fill="none" stroke="#fff" stroke-width="2"/></svg>
  </div>
  <div class="search-tab">
    <svg width="16" height="16" viewBox="0 0 16 16"><circle cx="6.5" cy="6.5" r="5" fill="none" stroke="#fff" stroke-width="2"/><path d="M10 10l5 5" stroke="#fff" stroke-width="2.4"/></svg>
    Serach shop space
  </div>
</section>

<main class="content">
  <section class="search-panel">
    <div class="field" style="left:24px;top:27px"><label>Shop Space For:</label><div class="select">Retail Malls</div></div>
    <div class="field" style="left:268px;top:27px"><label>Sale Or Rent Or Both:</label><div class="select">Both</div></div>
    <div class="field" style="left:512px;top:27px"><label>Select City:</label><div class="select">-Select-</div></div>
    <div class="field" style="left:755px;top:27px"><label>Select Locality/Micro-Market.</label><div class="select">-Select-</div></div>
    <div class="field" style="left:24px;top:103px"><label>Enter Keywords:</label><div class="input">Name of Project Delevoper etc</div></div>
    <div class="search-btn">Search</div>
    <div class="format-note">Select Retail Format: <a>Meaning of Retail Format</a></div>
  </section>

  <section class="about">
    <h2 class="section-title" style="top:50px">About <span>Lotvantage</span></h2>
    <p class="about-text">Lotvantage.com is a Specialised Web based platform for Retail Space, featuring properties across India under various formats such as Retail Malls, Shopping Complexes, High-street Shops.<br>Also featured are Retail Warehouses which provide the logistic back-end for the retail business. Lotvantage.com is useful to various category of users as follows-</p>

    <div class="category" style="left:43px">
      <svg width="90" height="84" viewBox="0 0 90 84"><circle cx="38" cy="40" r="26" fill="none" stroke="#c8c8c8" stroke-width="8"/><path d="M57 59l20 20" stroke="#c8c8c8" stroke-width="10" stroke-linecap="round"/><rect x="30" y="8" width="18" height="36" fill="var(--orange)"/></svg>
      <h3>Retail Malls</h3><p>Centrally Air-Conditioned</p>
    </div>
    <div class="category" style="left:275px">
      <svg width="90" height="84" viewBox="0 0 90 84"><circle cx="38" cy="40" r="26" fill="none" stroke="#c8c8c8" stroke-width="8"/><path d="M57 59l20 20" stroke="#c8c8c8" stroke-width="10" stroke-linecap="round"/><rect x="24" y="14" width="14" height="30" fill="var(--orange)"/><rect x="38" y="4" width="16" height="40" fill="var(--orange-dark)"/></svg>
      <h3>Shopping Complex</h3><p>Non Air-Conditioned Building</p>
    </div>
    <div class="category" style="left:499px">
      <svg width="90" height="84" viewBox="0 0 90 84"><circle cx="38" cy="40" r="26" fill="none" stroke="#c8c8c8" stroke-width="8"/><path d="M57 59l20 20" stroke="#c8c8c8" stroke-width="10" stroke-linecap="round"/><rect x="28" y="10" width="22" height="34" fill="var(--orange)"/></svg>
      <h3>High Street Shops</h3><p>Road Facing Retail</p>
    </div>
    <div class="category" style="left:738px">
      <svg width="90" height="84" viewBox="0 0 90 84"><circle cx="38" cy="40" r="26" fill="none" stroke="#c8c8c8" stroke-width="8"/><path d="M57 59l20 20" stroke="#c8c8c8" stroke-width="10" stroke-linecap="round"/><path d="M20 20h36l-4-10H24z" fill="var(--orange-dark)"/><rect x="24" y="20" width="28" height="24" fill="var(--orange)"/></svg>
      <h3>Retail Warehouses</h3><p>Back-end Retail Storage</p>
    </div>
  </section>

  <h2 class="section-title" style="top:522px">Featured <span>Projects</span></h2>

  <article class="card" style="left:26px;top:588px"><div class="card-photo" role="img" aria-label="Photo of glass towers at dusk" style="background:linear-gradient(160deg,#1d2c52,#5a6f9a 60%,#2a2f3c)"><span class="city-tag">Surat</span></div><div class="card-body"><div class="card-name">Corvell</div><div class="card-line">Estrin</div><div class="card-line">Shopping Complex</div><span class="view-btn">View the listing</span></div></article>
  <article class="card" style="left:270px;top:588px"><div class="card-photo" role="img" aria-label="Photo of a modern shopping complex under a blue sky" style="background:linear-gradient(180deg,#6f9bd0,#b9a68a 60%,#8a8a82)"><span class="city-tag">New Delhi</span></div><div class="card-body"><div class="card-name">Corvell</div><div class="card-line">Estrin</div><div class="card-line">Shopping Complex</div><span class="view-btn">View the listing</span></div></article>
  <article class="card" style="left:514px;top:588px"><div class="card-photo" role="img" aria-label="Photo of a lit mall facade in the evening" style="background:linear-gradient(180deg,#7a7c82,#5a3a24 60%,#c46a2a)"><span class="city-tag">Gurgaon</span></div><div class="card-body"><div class="card-name">Corvell</div><div class="card-line">Estrin</div><div class="card-line">Shopping Complex</div><span class="view-btn">View the listing</span></div></article>
  <article class="card" style="left:758px;top:588px"><div class="card-photo" role="img" aria-label="Photo of a busy mall atrium seen from above" style="background:linear-gradient(180deg,#6a6a6e,#a9a4a0 55%,#4c4a4a)"><span class="city-tag">Bhopal</span></div><div class="card-body"><div class="card-name">Corvell</div><div class="card-line">Estrin</div><div class="card-line">Shopping Complex</div><span class="view-btn">View the listing</span></div></article>

  <article class="card" style="left:26px;top:894px"><div class="card-photo" role="img" aria-label="Photo of a mall building lit at night" style="background:linear-gradient(180deg,#243a66,#55617a 55%,#b08a52)"><span class="city-tag">Surat</span></div><div class="card-body"><div class="card-name">Corvell</div><div class="card-line">Estrin</div><div class="card-line">Shopping Complex</div><span class="view-btn">View the listing</span></div></article>
  <article class="card" style="left:270px;top:894px"><div class="card-photo" role="img" aria-label="Photo of a white tensile roof mall atrium" style="background:linear-gradient(180deg,#c9d3de,#8fa6c2 55%,#6c7a8c)"><span class="city-tag">Chennai</span></div><div class="card-body"><div class="card-name">Corvell</div><div class="card-line">Estrin</div><div class="card-line">Shopping Complex</div><span class="view-btn">View the listing</span></div></article>
  <article class="card" style="left:514px;top:894px"><div class="card-photo" role="img" aria-label="Photo of a colourful mall exterior" style="background:linear-gradient(160deg,#3c6fb6,#b04a3a 55%,#8a8478)"><span class="city-tag">New Delhi</span></div><div class="card-body"><div class="card-name">Corvell</div><div class="card-line">Estrin</div><div class="card-line">Shopping Complex</div><span class="view-btn">View the listing</span></div></article>
  <article class="card" style="left:758px;top:894px"><div class="card-photo" role="img" aria-label="Photo of escalators inside a mall" style="background:linear-gradient(180deg,#3a3a3e,#7a6a5a 55%,#2e2e30)"><span class="city-tag">Surat</span></div><div class="card-body"><div class="card-name">Corvell</div><div class="card-line">Estrin</div><div class="card-line">Shopping Complex</div><span class="view-btn">View the listing</span></div></article>

  <h2 class="section-title" style="top:1221px">New <span>Launches</span></h2>

  <div class="carousel-arrow" style="left:0"><svg width="21" height="28" viewBox="0 0 21 28"><path d="M12 10l-4 4 4 4" fill="none" stroke="#555" stroke-width="1.5"/></svg></div>
  <div class="carousel-arrow" style="left:983px"><svg width="21" height="28" viewBox="0 0 21 28"><path d="M9 10l4 4-4 4" fill="none" stroke="#555" stroke-width="1.5"/></svg></div>

  <article class="launch" style="left:49px"><div class="card-photo" role="img" aria-label="Photo of a mall building under a blue sky" style="background:linear-gradient(180deg,#5a86c6,#b08a6e 60%,#7a6a5a)"><span class="city-tag">Surat</span></div><div class="launch-name">The Grand Arcade Place</div><div class="launch-sub">Kolar Road, Retail Malls</div><span class="view-btn">View the listing</span></article>
  <article class="launch" style="left:281px"><div class="card-photo" role="img" aria-label="Photo of a mall lit up at night" style="background:linear-gradient(180deg,#16203e,#3a3a5a 55%,#c0862e)"><span class="city-tag">Bhopal</span></div><div class="launch-name">The Grand Arcade Place</div><div class="launch-sub">Kolar Road, Retail Malls</div><span class="view-btn">View the listing</span></article>
  <article class="launch" style="left:513px"><div class="card-photo" role="img" aria-label="Photo of a mall interior with shoppers" style="background:linear-gradient(180deg,#4a3a2e,#a88a64 55%,#5a4a3a)"><span class="city-tag">Bangalore</span></div><div class="launch-name">The Grand Arcade Place</div><div class="launch-sub">Kolar Road, Retail Malls</div><span class="view-btn">View the listing</span></article>
  <article class="launch" style="left:745px"><div class="card-photo" role="img" aria-label="Photo of a large modern mall complex" style="background:linear-gradient(180deg,#7ea2d6,#a07a86 55%,#6a5a62)"><span class="city-tag">Mohali</span></div><div class="launch-name">The Grand Arcade Place</div><div class="launch-sub">Kolar Road, Retail Malls</div><span class="view-btn">View the listing</span></article>
</main>

<footer class="site-footer">
  <div class="foot-col" style="left:100px;width:240px">
    <h4>Editor's Choice</h4>
    <p style="margin-top:16px;text-align:justify">Lorem ipsum dolor sit amet, consectetuer adipiscing elit. Aenean commodo ligula eget dolor. Aenean massa. Cum sociis natoque penatibus et magnis dis parturient montes, nascetur ridiculus mus. Donec quam felis, ultricies nec, pellentesque</p>
  </div>
  <div class="foot-col" style="left:419px">
    <h4>Navigation</h4>
    <ul style="margin-top:16px"><li>About Us</li><li>Privacy Policy</li><li>Terms of Use</li><li>Contact Us</li><li>Site Map</li></ul>
  </div>
  <div class="foot-col" style="left:609px">
    <h4>Get in Touch</h4>
    <p style="margin-top:16px">Market Point, Unit 212, 2nd Floor,<br>Lorem Ipsum is simply,<br>Sector-9, Gurgaon - 122000<br>Phone : 000-000-0000<br>Fax : 000 - 000 - 0000</p>
  </div>
  <div class="foot-col" style="left:853px">
    <h4>Connect Online</h4>
    <div class="social"><span></span><span></span><span></span><span></span><span></span></div>
    <h4 style="margin-top:22px">Listing Alert</h4>
    <div class="alert-form"><div class="email">Email Address</div><div class="signup">SIGN UP</div></div>
  </div>
</footer>
<div class="copyright">© 2014 lotvantage &nbsp;|&nbsp; All Rights Reserved</div>

</body>
</html>
```